Professional business cards for real estate development company

I need business cards for my new real estate development company. The company, "KORVA" is a real estate development, investment, and advisory firm with a focus on multifamily, office, and mixed-use projects across primary and secondary markets in the Southeast United States.

Style preference is modern

Industry/Entity Type

Real Estate Development

Contact Information for Business Card

The business cards need to include:
Name
Title
Mailing Address
Phone Number
Web Address

Logo is attached. I would like white to be the primary color with incorporation of the company colors: #232D3A and #B5A451

Font styles to use
Other font styles liked:
• Montserrat, Avenir

Requirements
Must have
• Company Logo. No need to include the company name since the name is in the logo.
Should not have
• No line type designs

```html
<!DOCTYPE html>
<html lang="en">
<head>
<meta charset="utf-8">
<title>KORVA Business Cards</title>
<link href="https://fonts.googleapis.com/css2?family=Josefin+Sans:wght@300;400;600&display=swap" rel="stylesheet">
<style>
  :root {
    --navy: #232D3A;
    --navy-deep: #1c2430;
    --gold: #B5A451;
    --paper: #f4f4f2;
    --stage: #e6e6e4;
    --text-light: #d9dce0;
  }
  * { margin: 0; padding: 0; box-sizing: border-box; }
  html, body {
    width: 1200px; height: 801px; overflow: hidden;
    background: var(--stage);
    font-family: "Josefin Sans", sans-serif;
  }
  .sheet {
    position: relative; width: 1200px; height: 801px;
  }
  .card {
    position: absolute; top: 250px;
    width: 525px; height: 300px;
    box-shadow: 0 10px 30px rgba(0,0,0,0.12);
    overflow: hidden;
  }
  .card--back { left: 50px; display: flex; }
  .card--front { left: 625px; }

  .back-brand {
    width: 262px; height: 100%;
    background: var(--paper);
    display: flex; align-items: center; justify-content: center;
  }
  .back-info {
    flex: 1; height: 100%;
    background: var(--navy);
    padding: 58px 0 0 30px;
    color: var(--text-light);
  }
  .wordmark {
    display: flex; align-items: center; gap: 12px;
    font-weight: 600; letter-spacing: 3px;
  }
  .wordmark__square {
    width: 16px; height: 16px;
  }
  .wordmark--dark { color: var(--navy); font-size: 40px; }
  .wordmark--dark .wordmark__square { background: var(--navy); }
  .wordmark--light { color: var(--paper); font-size: 72px; }
  .wordmark--light .wordmark__square { background: var(--paper); width: 26px; height: 26px; }

  .person__name {
    color: var(--gold); font-size: 19px; font-weight: 400; letter-spacing: 1px;
  }
  .person__title {
    font-size: 13px; font-weight: 300; margin-top: 3px;
  }
  .address {
    font-size: 12.5px; font-weight: 300; line-height: 1.45; margin-top: 26px;
  }
  .contact { list-style: none; margin-top: 22px; }
  .contact li {
    display: flex; align-items: center; gap: 8px;
    font-size: 12px; font-weight: 300; margin-bottom: 6px;
  }
  .contact svg { width: 13px; height: 13px; flex-shrink: 0; }

  .front-photo {
    position: absolute; inset: 0;
    background: linear-gradient(135deg, #2a3342 0%, var(--navy) 45%, var(--navy-deep) 100%);
  }
  .front-brand {
    position: absolute; inset: 0;
    display: flex; align-items: center; justify-content: center;
  }
</style>
</head>
<body>
<main class="sheet">
  <section class="card card--back">
    <div class="back-brand">
      <div class="wordmark wordmark--dark"><span class="wordmark__square"></span>KORVA</div>
    </div>
    <div class="back-info">
      <h1 class="person__name">DANIEL EVERLY</h1>
      <p class="person__title">Partner</p>
      <p class="address">2140 Harlow Park NE<br>Atlanta, Georgia 30318</p>
      <ul class="contact">
        <li>
          <svg viewBox="0 0 14 14"><circle cx="7" cy="7" r="7" fill="var(--gold)"/><path d="M4.3 3.8c.4-.3.9-.2 1.1.2l.6 1.1c.2.3.1.7-.2.9l-.4.3c.4.9 1.1 1.6 2 2l.3-.4c.2-.3.6-.4.9-.2l1.1.6c.4.2.5.7.2 1.1-.6.8-1.5.9-2.4.4-1.4-.7-2.5-1.8-3.2-3.2-.5-.9-.4-1.8.4-2.4z" fill="var(--navy)"/></svg>
          000 0000 00 00
        </li>
        <li>
          <svg viewBox="0 0 14 14"><circle cx="7" cy="7" r="7" fill="var(--gold)"/><rect x="3.5" y="4.5" width="7" height="5" fill="none" stroke="var(--navy)" stroke-width="1"/><path d="M3.5 4.5l3.5 2.8 3.5-2.8" fill="none" stroke="var(--navy)" stroke-width="1"/></svg>
          info@korvadevelopment.com
        </li>
        <li>
          <svg viewBox="0 0 14 14"><circle cx="7" cy="7" r="7" fill="var(--gold)"/><circle cx="7" cy="7" r="3.6" fill="none" stroke="var(--navy)" stroke-width="1"/><path d="M3.4 7h7.2M7 3.4c-1.5 2-1.5 5.2 0 7.2M7 3.4c1.5 2 1.5 5.2 0 7.2" fill="none" stroke="var(--navy)" stroke-width="0.8"/></svg>
          www.korvadevelopment.com
        </li>
      </ul>
    </div>
  </section>

  <section class="card card--front">
    <div class="front-photo" role="img" aria-label="Dark navy-toned photograph of glass office towers seen from below"></div>
    <div class="front-brand">
      <div class="wordmark wordmark--light"><span class="wordmark__square"></span>KORVA</div>
    </div>
  </section>
</main>
</body>
</html>
```